Label Design for a sexy ladies 5 pocket skinny

We need modern packaging design for women's skinny 5 pocket pants for a brand name Tarnel. All kinds of packaging designs are welcome.
The pant is folded and packaged in a poly bag. We require a label design for the brand name Tarnel. The main label will be attached by a string on the belt loop. the size of that label will 25cm in length and 10cm wide. This is the first label the customer see's when she picks up the garment. Therefore, we require an eye catching design for that. If required it could have certain information about the pant on the main label such as Comfort fit, Wrinkle-resistant, machine washable, luxury fabric. But, if you feel that adding the above information spoils the design of the label then it is not a must to include the above information. On the back of the label we like to include the information that this pant was manufactured in an Oskel Platinum certified green plant and hence the damage to the environment because of the plant is nill.
The second label is attached on to the waist band and the purpose of that label is to include the size of the pant such 32x32. The size of that label is 8cm in length and 4cm in width. There is no design on the back on this label it has to be blank.
Sample is given for what we currently use for our mens chino pant. we are looking for something very different.
Reason: because there was a delay in the project being approved by pixel harbor.
Environment

```html
<!DOCTYPE html>
<html lang="en">
<head>
<meta charset="utf-8">
<title>Tarnel Women's Skinny Labels</title>
<link rel="stylesheet" href="https://fonts.googleapis.com/css2?family=Bodoni+Moda:ital,wght@0,700;1,500&family=Montserrat:wght@500;700&display=swap">
<style>
  :root {
    --plum: #2b1431;
    --plum-deep: #1d0c22;
    --blush: #f3b9c8;
    --blush-soft: #f9dbe3;
    --gold: #d9a441;
    --ivory: #fbf4ee;
    --canvas: #ffffff;
  }
  * { box-sizing: border-box; margin: 0; padding: 0; }
  html, body { width: 1200px; height: 926px; overflow: hidden; background: var(--canvas); }
  .canvas { position: relative; width: 1200px; height: 926px; }

  .tag {
    position: absolute;
    border-radius: 6px;
    overflow: hidden;
    box-shadow: 2px 3px 6px rgba(40, 20, 40, 0.45);
    text-align: center;
  }
  .tag--main-front, .tag--main-back { background: var(--plum); width: 244px; height: 730px; top: 78px; }
  .tag--main-front { left: 274px; }
  .tag--main-back { left: 578px; }
  .tag--size { left: 869px; top: 245px; width: 207px; height: 408px; background: var(--blush); }

  .tag__frame {
    position: absolute; inset: 12px;
    border: 1.5px solid var(--gold);
    border-radius: 3px;
    pointer-events: none;
  }
  .tag__eyelet {
    position: absolute; left: 50%; top: 26px;
    width: 14px; height: 14px; margin-left: -7px;
    border-radius: 50%;
    background: var(--canvas);
    border: 2px solid var(--gold);
  }

  .brand-name {
    position: absolute; left: 0; right: 0;
    font-family: "Bodoni Moda", Didot, serif;
    font-weight: 700;
    color: var(--ivory);
    letter-spacing: 5px;
    padding-left: 5px;
    white-space: nowrap;
  }
  .tag--main-front .brand-name { top: 70px; font-size: 38px; line-height: 48px; }
  .tag--main-back .brand-name { top: 62px; font-size: 24px; line-height: 32px; letter-spacing: 4px; }

  .gold-rule {
    position: absolute; left: 50%;
    height: 1.5px; background: var(--gold);
  }
  .tag--main-front .gold-rule { top: 134px; width: 80px; margin-left: -40px; }
  .tag--main-back .gold-rule { top: 108px; width: 56px; margin-left: -28px; }

  .product-arch {
    position: absolute; left: 32px; top: 170px;
    width: 180px; height: 350px;
    border-radius: 90px 90px 6px 6px;
    background: linear-gradient(180deg, var(--blush-soft), var(--blush));
    color: var(--plum);
  }
  .product-arch__for {
    position: absolute; left: 0; right: 0; top: 128px;
    font-family: "Bodoni Moda", Didot, serif;
    font-style: italic; font-weight: 500;
    font-size: 26px; line-height: 32px;
  }
  .product-arch__cut {
    position: absolute; left: 0; right: 0; top: 172px;
    font-family: "Montserrat", Arial, sans-serif;
    font-weight: 700;
    font-size: 12px; line-height: 18px;
    letter-spacing: 3px; padding-left: 3px;
    text-transform: uppercase;
  }
  .product-arch__style {
    position: absolute; left: 0; right: 0; top: 196px;
    font-family: "Bodoni Moda", Didot, serif;
    font-style: italic; font-weight: 500;
    font-size: 42px; line-height: 52px;
  }
  .product-arch__dot {
    position: absolute; left: 50%; top: 280px;
    width: 10px; height: 10px; margin-left: -5px;
    border-radius: 50%; background: var(--plum);
  }

  .feature-list {
    position: absolute; left: 0; right: 0; top: 560px;
    list-style: none;
    font-family: "Montserrat", Arial, sans-serif;
    font-weight: 500;
    font-size: 11px; line-height: 26px;
    letter-spacing: 2px; padding-left: 2px;
    text-transform: uppercase;
    color: var(--ivory);
  }
  .feature-list li + li { border-top: 1px solid rgba(217, 164, 65, 0.45); margin: 0 44px; }
  .feature-list li:first-child { margin: 0 44px; }

  .certificate-seal {
    position: absolute; left: 50%; top: 150px;
    width: 110px; height: 110px; margin-left: -55px;
    border-radius: 50%;
    background: var(--gold);
    box-shadow: 0 0 0 6px var(--plum), 0 0 0 7.5px var(--gold);
  }

  .eco-statement {
    position: absolute; left: 28px; right: 28px; top: 300px;
    font-family: "Bodoni Moda", Didot, serif;
    font-style: italic; font-weight: 500;
    font-size: 17px; line-height: 27px;
    color: var(--ivory);
  }
  .eco-statement strong {
    font-family: "Montserrat", Arial, sans-serif;
    font-style: normal; font-weight: 700;
    font-size: 12px; letter-spacing: 2px;
    text-transform: uppercase; color: var(--gold);
  }

  .back-band {
    position: absolute; left: 0; right: 0; bottom: 0; height: 150px;
    background: var(--blush);
    border-radius: 120px 120px 0 0 / 40px 40px 0 0;
  }
  .back-band__care {
    position: absolute; left: 0; right: 0; bottom: 58px;
    font-family: "Montserrat", Arial, sans-serif;
    font-weight: 700;
    font-size: 11px; line-height: 18px;
    letter-spacing: 3px; padding-left: 3px;
    text-transform: uppercase;
    color: var(--plum);
  }

  .size-readout {
    position: absolute; inset: 0;
    display: flex; flex-direction: column; justify-content: center; align-items: center;
    color: var(--plum);
    border: 1.5px solid var(--plum);
    border-radius: 3px;
    margin: 10px;
  }
  .size-readout__number {
    font-family: "Bodoni Moda", Didot, serif;
    font-weight: 700;
    font-size: 76px; line-height: 84px;
  }
  .size-readout__word {
    font-family: "Montserrat", Arial, sans-serif;
    font-weight: 700;
    font-size: 14px; line-height: 22px;
    letter-spacing: 4px; padding-left: 4px;
    text-transform: uppercase;
  }
  .size-readout__times {
    font-family: "Bodoni Moda", Didot, serif;
    font-style: italic; font-weight: 500;
    font-size: 30px; line-height: 44px;
  }
</style>
</head>
<body>
<main class="canvas">

  <section class="tag tag--main-front">
    <div class="tag__frame"></div>
    <div class="tag__eyelet"></div>
    <div class="brand-name">TARNEL</div>
    <div class="gold-rule"></div>
    <div class="product-arch">
      <div class="product-arch__for">Women’s</div>
      <div class="product-arch__cut">5 Pocket</div>
      <div class="product-arch__style">Skinny</div>
      <div class="product-arch__dot"></div>
    </div>
    <ul class="feature-list">
      <li>Comfort fit</li>
      <li>Wrinkle-resistant</li>
      <li>Machine washable</li>
      <li>Luxury fabric</li>
    </ul>
  </section>

  <section class="tag tag--main-back">
    <div class="tag__frame"></div>
    <div class="tag__eyelet"></div>
    <div class="brand-name">TARNEL</div>
    <div class="gold-rule"></div>
    <div class="certificate-seal" aria-hidden="true"></div>
    <p class="eco-statement">
      This Tarnel skinny was proudly made in an
      <strong>Oskel Platinum</strong>
      certified green plant, so its impact on the environment is nil.
    </p>
    <div class="back-band"></div>
    <div class="back-band__care">Made with care</div>
  </section>

  <section class="tag tag--size">
    <div class="size-readout">
      <span class="size-readout__number">32</span>
      <span class="size-readout__word">Waist</span>
      <span class="size-readout__times">x</span>
      <span class="size-readout__number">32</span>
      <span class="size-readout__word">Length</span>
    </div>
  </section>

</main>
</body>
</html>
```